Pressleaf Design Project

I am looking for a designer that can help me with to design a theme for www.maptrellis.example.

Our website is a map based business directory for things that are great for kids. The name of the website will be www.pipandrue.example. As you can see, we have already applied theme but we are not happy with the design.

We feel it is too old, stale and looks like a "theme" and would like to completely overhaul the design to give it our own flavour.

This project will require the designer to design 5 pages (uncoded) based on the maptrellis pressleaf theme.

The pages are:
1) Homepage
2) Business Listing Page
3) Business Details Page
4) Add Listing Page
5) Blog Page (This is page should be more than just a listing of blogs. Imagine designing this as if were the homepage of a blog. It needs to be attention grabbing)

In addition, we would like to you to design custom map pointers that are suitable for the categories:

1) Food - Kids friendly places
2) Inside - Things to do indoor (Cinema, Ice Skating etc)
3) Learn - Classes, Course, Etc
4) Outside - Things to do outside (Zoo, Parks, Bike Riding)
5) Services - service for kids (doctors, babysitting)
6) Shop - Kids Stores
7) Events - Upcoming Events

One of things that we don't like about the current design is that it feels too "blocky" with no differentiation between the various sections of the homepage.

Some websites that we like are:

1) www.silk-a-vanta.example
2) www.fernbeacon.example

Please propose stock photography, icons etc where appropriate

The theme is very flexible. Some other websites that have also used www.maptrellis.example are:
1) http://www.campusgrid.example/
2) http://www.cotsandcradles.example/
3) http://www.ripristino-file-vault.example/

These are just for your reference to showcase the flexibility of the theme and NOT as a design reference because they are all not what we are looking for.

KEYWORDS: modern, clean, not blocky, stylish, urban, bold, feminine, youthful, simple, subtle

TARGET: Upwardly mobile mums, professional mums, modern mums that are into fashion, sipping coffee at inner city cafes

Hi everyone,

Here are some of the websites that we like with comments.

https://files.boxvane.example/u/7419052/Designswelike.pdf

Thanks
Marcus

Thank you for everyone that is working on a design for Pip and Rue. The contest will be closing in 1 day so I hope to see more designs. There are some designs that we feel have potential but we are open minded. To all the designers that we have provided feedback to, I hope that I see the comments come to life.

Thanks
Marcus

Target Market(s)

Mums

Industry/Entity Type

Business Directory

Requirements
Must have
• - The map must be the centre of attention of the design - at the moment, it feels a little small. Make the map larger.
- Map icons must be redesigned.
- The rating system needs to be redesigned. We dont like the stars.

```html
<!DOCTYPE html>
<html lang="en">
<head>
<meta charset="utf-8">
<title>Pip and Rue</title>
<link href="https://fonts.googleapis.com/css2?family=Arimo:wght@400;700&family=Roboto+Condensed:wght@400;700&display=swap" rel="stylesheet">
<style>
:root{
  --bg:#000;
  --bar:#161616;
  --panel:#1c1c1c;
  --teal:#1ea3c3;
  --teal-dark:#0b6479;
  --text:#c9c9c9;
  --white:#fff;
  --green:#4ab520;
  --gold:#f2b705;
  --map-land:#e9e6da;
  --map-water:#c4d6e4;
}
*{box-sizing:border-box;margin:0;padding:0}
html,body{width:720px;height:1200px;overflow:hidden;background:var(--bg)}
body{position:relative;font-family:Arimo,Arial,sans-serif;color:var(--text);font-size:8px}
.abs{position:absolute}
.topbar{left:0;top:0;width:720px;height:25px;background:var(--bar)}
.welcome{left:562px;top:8px;font-size:8px;color:#ddd;white-space:nowrap}
.topbar svg{position:absolute;top:6px}
.brand{left:50px;top:36px;font-size:38px;color:var(--teal);font-weight:400;letter-spacing:1px}
.social{left:555px;top:37px;display:flex;gap:4px}
.social span{width:17px;height:17px;background:var(--teal);border-radius:2px}
.search{top:67px;height:17px;background:#e2e2e2;border:1px solid #888;font-size:7px;font-weight:700;color:#222;padding:4px 0 0 18px}
.search svg{position:absolute;left:4px;top:3px}
.go{left:656px;top:67px;width:20px;height:17px;background:var(--teal)}
.nav{left:44px;top:98px;width:632px;height:27px;display:flex}
.nav a{color:var(--white);font-size:9px;text-decoration:none;padding-top:10px;text-align:center;border-right:1px solid #333;height:27px;white-space:nowrap}
.nav a.active{background:var(--teal)}
.map{left:44px;top:125px;width:632px;height:269px;border:2px solid var(--teal);background:linear-gradient(160deg,var(--map-water) 0%,var(--map-land) 30%,#ede7d3 60%,var(--map-water) 100%);overflow:hidden}
.map-ui{left:46px;top:127px;width:628px;height:265px}
.toggle{left:600px;top:131px;display:flex;border:1px solid #999;background:#fff;font-size:8px;font-weight:700;color:#222}
.toggle span{padding:2px 5px}
.toggle span+span{border-left:1px solid #999;font-weight:400;color:#444}
.cats{left:594px;top:166px;width:84px}
.cat{height:23px;margin-bottom:7px;background:#3b3b3b;color:var(--white);font-size:9px;font-weight:700;padding:6px 0 0 34px;position:relative;clip-path:polygon(10px 0,100% 0,100% 100%,10px 100%,0 50%)}
.cat.active{background:var(--teal)}
.cat i{position:absolute;left:14px;top:5px;width:13px;height:13px;border-radius:50%;background:#ccc}
.cat.active i{background:#8ad13c}
.feat-title{top:411px;font-family:"Roboto Condensed",Arial,sans-serif;font-size:16px;color:var(--teal)}
.strip{left:44px;top:434px;width:632px;height:129px;background:#2a2a2a}
.strip .arrow{position:absolute;top:0;width:30px;height:129px;background:#3a3a3a}
.strip .arrow svg{position:absolute;left:6px;top:45px}
.card{position:absolute;top:0;width:189px;height:129px}
.card p{background:var(--teal-dark);height:37px;color:var(--white);font-size:7.5px;line-height:11px;padding:7px 8px}
.card .photo{height:92px}
.card .posted{position:absolute;right:0;bottom:0;width:128px;height:21px;background:rgba(0,0,0,.75);color:var(--white);font-size:7.5px;padding:6px 0 0 8px}
.section-title{font-family:"Roboto Condensed",Arial,sans-serif;font-size:13px;color:var(--teal);padding-bottom:3px;border-bottom:1px solid #444}
.pager{left:366px;top:585px;display:flex;gap:6px;align-items:center;font-size:7px;color:#888}
.pager b{width:12px;height:12px;background:#333;color:#fff;text-align:center;line-height:12px}
.pager em{width:13px;height:13px;background:#444;margin-left:-3px}
.pager em.first{margin-left:4px}
.pager em.on{background:var(--teal)}
.review{width:208px}
.review .photo{height:114px}
.thumbs{height:14px;margin-top:7px;text-align:right}
.review p{font-size:7.5px;line-height:11.5px;color:#aaa;margin-top:2px;text-align:justify}
.meta{display:flex;justify-content:space-between;margin-top:7px;font-size:7.5px;font-weight:700}
.meta span{color:var(--teal)}
.meta a{color:var(--white)}
.divider{left:44px;width:429px;height:1px;background:linear-gradient(90deg,transparent,#555,transparent)}
.vdiv{left:258px;width:1px;background:#2a2a2a}
.tabs{left:487px;top:583px;width:189px;height:23px;display:flex}
.tabs span{flex:1;background:var(--white);color:#555;font-size:8px;font-weight:700;text-align:center;padding-top:7px;border-left:1px solid #ccc}
.tabs span.on{background:var(--panel);color:var(--white);border:0}
.promo{left:487px;top:606px;width:189px;height:134px;background:linear-gradient(#2a2a2a,#111)}
.promo h3{position:absolute;left:17px;top:9px;font-size:19px;color:var(--white);font-weight:700}
.promo ul{position:absolute;left:12px;top:44px;list-style:none}
.promo li{font-size:13px;color:var(--white);margin-bottom:7px;padding-left:15px;position:relative}
.promo li:before{content:"";position:absolute;left:0;top:5px;width:7px;height:7px;background:var(--green)}
.promo .site{position:absolute;left:11px;bottom:5px;font-size:11px;font-weight:700;color:var(--white)}
.promo svg{position:absolute;right:12px;top:62px}
.news{left:487px;top:753px;width:189px;height:80px;border:3px solid var(--teal-dark);background:#111}
.news h4{background:var(--teal-dark);color:var(--white);font-size:9px;height:20px;padding:4px 0 0 8px}
.news p{font-size:9px;font-weight:700;color:#aaa;padding:5px 0 0 8px}
.news .field{position:absolute;left:11px;top:46px;width:165px;height:20px;border:2px solid #555;background:#fff;font-size:7px;color:#777;padding:4px 6px}
.news .field b{position:absolute;right:0;top:0;height:16px;width:36px;background:var(--teal);color:#fff;font-size:7.5px;padding-top:3px;text-align:center;font-weight:400}
.ad{left:487px;top:848px;width:189px;height:157px;background:#2c2c2c}
.ad .inner{position:absolute;left:4px;top:4px;width:181px;height:149px;background:linear-gradient(#f0f0f0,#c9c9c9);text-align:center;color:#333}
.ad .t1{margin-top:16px;font-size:17px;font-weight:700;color:#bbb;letter-spacing:1px}
.ad .t2{font-size:12px;margin-top:2px}
.ad .t3{font-size:10px;margin-top:8px}
.ad .t4{margin:14px auto 0;width:140px;font-size:12px;font-weight:700;color:#999;letter-spacing:1px;display:flex;align-items:center;gap:6px;justify-content:center;white-space:nowrap}
.ad .t4 i{width:14px;height:14px;border-radius:50%;background:#999;flex:none}
.footer{left:0;top:1018px;width:720px;height:150px;background:#111}
.col{top:10px;width:190px}
.col h5{font-family:"Roboto Condensed",Arial,sans-serif;font-weight:700;font-size:11px;color:var(--teal);padding-bottom:3px;border-bottom:1px solid #333;display:inline-block;width:64px}
.quote{font-size:7.5px;line-height:11.5px;color:#999;margin-top:12px;padding-left:16px;position:relative}
.quote:before{content:"\201C";position:absolute;left:0;top:-6px;font-size:24px;color:#333}
.item{margin-top:10px;font-size:7.5px;line-height:11px;color:#999;padding-bottom:5px;border-bottom:1px dashed #333}
.item b{display:block;color:var(--white);margin-bottom:2px}
.item strong{color:var(--white)}
.bottom{left:0;top:1170px;width:720px;height:30px;background:#0a0a0a;font-size:7px;color:#777}
.bottom .links{position:absolute;left:44px;top:11px}
.bottom .copy{position:absolute;right:44px;top:11px}
</style>
</head>
<body>
<svg width="0" height="0" style="position:absolute">
  <defs>
    <symbol id="thumb" viewBox="0 0 10 10"><path d="M1 4h2v6H1zM4 4l2-4c1 0 1.5.6 1.3 1.6L7 4h2.2c.6 0 .9.5.8 1l-1 4c-.1.6-.5 1-1 1H4z"/></symbol>
    <symbol id="pin" viewBox="0 0 22 30"><rect x="1" y="1" width="20" height="20" rx="3"/><path d="M7 21h8l-4 7z"/><circle cx="11" cy="11" r="4.5" fill="#fff" opacity=".85"/></symbol>
  </defs>
</svg>

<header class="abs topbar">
  <span class="abs welcome">Welcome, Guest</span>
  <svg style="left:628px" width="10" height="12" viewBox="0 0 10 12"><circle cx="5" cy="3.5" r="2.5" fill="#ddd"/><rect x="4" y="5" width="2" height="6" fill="#ddd"/></svg>
  <span class="abs" style="left:645px;top:7px;color:#ddd">/</span>
  <svg style="left:655px" width="10" height="12" viewBox="0 0 10 12"><path d="M2.5 5V3.5a2.5 2.5 0 0 1 5 0V5" stroke="#ddd" fill="none" stroke-width="1.4"/><rect x="1" y="5" width="8" height="6" fill="#ddd"/></svg>
</header>

<div class="abs brand">pip &amp; rue</div>
<div class="abs social"><span></span><span></span><span></span><span></span><span></span><span></span></div>

<div class="abs search" style="left:414px;width:134px">
  <svg width="10" height="10" viewBox="0 0 10 10"><circle cx="4" cy="4" r="3" stroke="#1b6f84" stroke-width="1.5" fill="none"/><path d="M6.2 6.2L9 9" stroke="#1b6f84" stroke-width="1.6"/></svg>Search...
</div>
<div class="abs search" style="left:550px;width:104px">
  <svg width="10" height="10" viewBox="0 0 10 10"><circle cx="5" cy="5" r="4" stroke="#1b6f84" stroke-width="1.5" fill="none"/><path d="M3 7l4-4" stroke="#1b6f84" stroke-width="1.5"/></svg>Near...
</div>
<div class="abs go"><svg width="20" height="17" viewBox="0 0 20 17"><path d="M5 8.5h9M10 4.5l4 4-4 4" stroke="#fff" stroke-width="1.6" fill="none"/></svg></div>

<nav class="abs nav">
  <a class="active" href="#" style="width:59px">HOME</a>
  <a href="#" style="width:110px">BUSINESS LISTING</a>
  <a href="#" style="width:111px">BUSINESS DETAILS</a>
  <a href="#" style="width:87px">ADD LISTING</a>
  <a href="#" style="width:55px;border:0">BLOG</a>
</nav>

<div class="abs map" role="img" aria-label="Street map of the city and its coastline, showing roads, districts and waterways"></div>
<svg class="abs map-ui" width="628" height="265" viewBox="0 0 628 265" aria-hidden="true">
  <circle cx="28" cy="29" r="15" fill="#f4f4f4" stroke="#999"/>
  <path d="M28 18l-3 4h6zM28 40l-3-4h6zM17 29l4-3v6zM39 29l-4-3v6z" fill="#777"/>
  <rect x="22" y="57" width="12" height="22" rx="2" fill="#f4f4f4" stroke="#aaa"/>
  <circle cx="28" cy="63" r="2.5" fill="#e39a17"/><rect x="26" y="66" width="4" height="9" fill="#e39a17"/>
  <rect x="22" y="90" width="11" height="11" fill="#fff" stroke="#999"/><path d="M25 95.5h5M27.5 93v5" stroke="#555"/>
  <rect x="27" y="101" width="1" height="118" fill="#999"/>
  <rect x="22" y="219" width="11" height="11" fill="#fff" stroke="#999"/><path d="M25 224.5h5" stroke="#555"/>
  <use href="#pin" x="184" y="116" width="22" height="30" fill="#5aa52a"/>
  <use href="#pin" x="226" y="100" width="22" height="30" fill="#e0742a"/>
  <use href="#pin" x="297" y="96" width="22" height="30" fill="#c04bb0"/>
  <use href="#pin" x="357" y="76" width="22" height="30" fill="#3f7d2a"/>
  <use href="#pin" x="356" y="120" width="22" height="30" fill="#2f74c9"/>
  <use href="#pin" x="257" y="145" width="22" height="30" fill="#6d58b8"/>
  <use href="#pin" x="312" y="162" width="22" height="30" fill="#c99a1e"/>
</svg>
<div class="abs toggle"><span>Map</span><span>Satellite</span></div>
<div class="abs cats">
  <div class="cat active"><i></i>Food</div>
  <div class="cat"><i></i>Inside</div>
  <div class="cat"><i></i>Learn</div>
  <div class="cat"><i></i>Outside</div>
  <div class="cat"><i></i>Services</div>
  <div class="cat"><i></i>Shop</div>
  <div class="cat"><i></i>Events</div>
</div>

<h2 class="abs feat-title" style="left:75px">Food</h2>
<h2 class="abs feat-title" style="left:265px">Learn</h2>
<h2 class="abs feat-title" style="left:455px">Shop</h2>
<section class="abs strip">
  <div class="arrow" style="left:0"><svg width="18" height="40" viewBox="0 0 18 40"><path d="M15 2L3 20l12 18" stroke="#ddd" stroke-width="4" fill="none"/></svg></div>
  <article class="card" style="left:31px">
    <p>Lorem Ipsum is simply dummy text of the printing and typesetting industry. Lorem Ipsum has been the</p>
    <div class="photo" role="img" aria-label="Fresh fruit and vegetables" style="background:linear-gradient(135deg,#7a9a2a,#c8421e 50%,#e3a21c)"></div>
    <div class="posted">Posted by admin on 11 Sep,2012</div>
  </article>
  <article class="card" style="left:221px">
    <p>Lorem Ipsum is simply dummy text of the printing and typesetting industry. Lorem Ipsum has been the</p>
    <div class="photo" role="img" aria-label="Child studying at a desk" style="background:linear-gradient(135deg,#d9d4cc,#b7a48c 60%,#8a6f55)"></div>
    <div class="posted">Posted by admin on 11 Sep,2012</div>
  </article>
  <article class="card" style="left:411px">
    <p>Lorem Ipsum is simply dummy text of the printing and typesetting industry. Lorem Ipsum has been the</p>
    <div class="photo" role="img" aria-label="Woman at a cafe with cupcakes" style="background:linear-gradient(135deg,#e8ddd2,#c79a86 55%,#8c4c3b)"></div>
    <div class="posted">Posted by admin on 11 Sep,2012</div>
  </article>
  <div class="arrow" style="left:602px"><svg width="18" height="40" viewBox="0 0 18 40"><path d="M3 2l12 18L3 38" stroke="#ddd" stroke-width="4" fill="none"/></svg></div>
</section>

<h2 class="abs section-title" style="left:44px;top:580px">Latest Reviews</h2>
<div class="abs pager"><span>1</span><b>2</b><span>3</span><span>4</span><span>››</span><em class="first"></em><em class="on"></em></div>

<article class="abs review" style="left:44px;top:606px">
  <div class="photo" role="img" aria-label="Bowl of fresh salad" style="background:linear-gradient(135deg,#2d3b1a,#5e8a2a 45%,#b2311c)"></div>
  <div class="thumbs"><svg width="62" height="10" viewBox="0 0 62 10"><use href="#thumb" x="0" width="10" height="10" fill="#1ea3c3"/><use href="#thumb" x="13" width="10" height="10" fill="#1ea3c3"/><use href="#thumb" x="26" width="10" height="10" fill="#fff"/><use href="#thumb" x="39" width="10" height="10" fill="#fff"/><use href="#thumb" x="52" width="10" height="10" fill="#fff"/></svg></div>
  <p>Lorem Ipsum is simply dummy text of the printing and typesetting industry. Lorem Ipsum has been the industry's standard dummy text ever since the 1500s, when</p>
  <div class="meta"><span>Lorem Ipsum &nbsp;|&nbsp; 11 Sep.2012</span><a>More Info ››</a></div>
</article>
<article class="abs review" style="left:265px;top:606px">
  <div class="photo" role="img" aria-label="Students in a classroom" style="background:linear-gradient(135deg,#c9b9a6,#3d6fb0 55%,#b8322a)"></div>
  <div class="thumbs"><svg width="62" height="10" viewBox="0 0 62 10"><use href="#thumb" x="0" width="10" height="10" fill="#1ea3c3"/><use href="#thumb" x="13" width="10" height="10" fill="#1ea3c3"/><use href="#thumb" x="26" width="10" height="10" fill="#fff"/><use href="#thumb" x="39" width="10" height="10" fill="#fff"/><use href="#thumb" x="52" width="10" height="10" fill="#fff"/></svg></div>
  <p>Lorem Ipsum is simply dummy text of the printing and typesetting industry. Lorem Ipsum has been the industry's standard dummy text ever since the 1500s, when</p>
  <div class="meta"><span>Lorem Ipsum &nbsp;|&nbsp; 11 Sep.2012</span><a>More Info ››</a></div>
</article>
<div class="abs divider" style="top:803px"></div>
<div class="abs vdiv" style="top:745px;height:50px"></div>
<article class="abs review" style="left:44px;top:818px">
  <div class="photo" role="img" aria-label="Family relaxing in a garden" style="background:linear-gradient(180deg,#e9ece4,#7fa24a 55%,#3f6b22)"></div>
  <div class="thumbs"><svg width="62" height="10" viewBox="0 0 62 10"><use href="#thumb" x="0" width="10" height="10" fill="#1ea3c3"/><use href="#thumb" x="13" width="10" height="10" fill="#1ea3c3"/><use href="#thumb" x="26" width="10" height="10" fill="#1ea3c3"/><use href="#thumb" x="39" width="10" height="10" fill="#1ea3c3"/><use href="#thumb" x="52" width="10" height="10" fill="#fff"/></svg></div>
  <p>Lorem Ipsum is simply dummy text of the printing and typesetting industry. Lorem Ipsum has been the industry's standard dummy text ever since the 1500s, when</p>
  <div class="meta"><span>Lorem Ipsum &nbsp;|&nbsp; 11 Sep.2012</span><a>More Info ››</a></div>
</article>
<article class="abs review" style="left:265px;top:818px">
  <div class="photo" role="img" aria-label="Parent and teen talking in a kitchen" style="background:linear-gradient(135deg,#e6e1d8,#a08a74 55%,#4a3a32)"></div>
  <div class="thumbs"><svg width="62" height="10" viewBox="0 0 62 10"><use href="#thumb" x="0" width="10" height="10" fill="#1ea3c3"/><use href="#thumb" x="13" width="10" height="10" fill="#1ea3c3"/><use href="#thumb" x="26" width="10" height="10" fill="#1ea3c3"/><use href="#thumb" x="39" width="10" height="10" fill="#fff"/><use href="#thumb" x="52" width="10" height="10" fill="#fff"/></svg></div>
  <p>Lorem Ipsum is simply dummy text of the printing and typesetting industry. Lorem Ipsum has been the industry's standard dummy text ever since the 1500s, when</p>
  <div class="meta"><span>Lorem Ipsum &nbsp;|&nbsp; 11 Sep.2012</span><a>More Info ››</a></div>
</article>
<div class="abs vdiv" style="top:957px;height:50px"></div>

<div class="abs tabs"><span class="on">Lorem ipsum</span><span>Lorem</span><span>Lorem</span></div>
<aside class="abs promo">
  <h3>Lorem <span style="font-weight:400">ipsum</span></h3>
  <ul><li>Lorem ipsum dolor</li><li>Lorem ipsu</li><li>Ipsum Lor</li></ul>
  <svg width="40" height="40" viewBox="0 0 40 40"><polygon points="20,2 25,15 39,15 28,24 32,38 20,30 8,38 12,24 1,15 15,15" fill="var(--gold)"/></svg>
  <div class="site">www.sitename.example</div>
</aside>

<aside class="abs news">
  <h4>Newsletter Subscribe</h4>
  <p>If you did like to stay up-</p>
  <div class="field">Email Address<b>Submit</b></div>
</aside>

<aside class="abs ad">
  <div class="inner">
    <div class="t1">maptrellis</div>
    <div class="t2">Pressleaf Framework</div>
    <div class="t3">available soon on</div>
    <div class="t4"><i></i>STITCH STUDIO</div>
  </div>
</aside>

<footer class="abs footer">
  <div class="abs col" style="left:44px">
    <h5>Testimonial</h5>
    <p class="quote">Lorem Ipsum is simply dummy text of the printing and typesetting industry. Lorem Ipsum has been the industry's standard dummy text ever since the 1500s, when an unknown printer took a galley of type and scrambled it to make a type specimen book. It has survived not only five centuries, but also the leap into electronic typesetting, remaining essentially unchanged.</p>
  </div>
  <div class="abs col" style="left:265px">
    <h5>Latest News</h5>
    <div class="item"><b>A Weekend on the Parkway</b>Lorem ipsum dolor sit amet, consectetuer adipiscing elit. Praesent aliquam, justo convallis luctus rutrum,<br><strong>10 September, 2012</strong></div>
    <div class="item" style="border:0"><b>A Weekend on the Parkway</b>Lorem ipsum dolor sit amet, consectetuer adipiscing elit. Praesent aliquam, justo convallis luctus rutrum,<br><strong>10 September, 2012</strong></div>
  </div>
  <div class="abs col" style="left:487px">
    <h5>Tag Cloud</h5>
    <div class="item"><b>A Weekend on the Parkway</b>Lorem ipsum dolor sit amet, consectetuer adipiscing elit. Praesent aliquam, justo convallis luctus rutrum,<br><strong>Read More ››</strong></div>
    <div class="item" style="border:0"><b>A Weekend on the Parkway</b>Lorem ipsum dolor sit amet, consectetuer adipiscing elit. Praesent aliquam, justo convallis luctus rutrum,<br><strong>Read More ››</strong></div>
  </div>
</footer>
<div class="abs bottom">
  <span class="links">Home &nbsp;|&nbsp; Business Listing &nbsp;|&nbsp; Business Details &nbsp;|&nbsp; Add Listing &nbsp;|&nbsp; Blog</span>
  <span class="copy">Copyright © 2012-2013, pipandrue, All Rights Reserved</span>
</div>
</body>
</html>
```